Bref créative
Stationery - Business Card / Letterhead
For Public Adjusting Company
Professional
Doran T. Whitcombe
Sr. Public Adjuster
58 W. Alder St.
Suite 612
Smithtown, NY 11492
doran@trclaimpro.com
www.trclaimpro.com
On the front I want our logo with the shadow on the bottom
On the back I would like you to incorporate a little creative usage of either the shield/lighthouse logo and all of my information
This logo should be used as the front as it has the bottom shadow which for some reason is not showing up on the other logos
the business card front will be high gloss finish
Also the fax number should be 516.843.9075 not 829. there is no where else for me to edit that once the project is uploaded

```html
<!DOCTYPE html>
<html lang="en">
<head>
<meta charset="utf-8">
<title>TR Claim Advisors – Stationery</title>
<link href="https://fonts.googleapis.com/css2?family=Cinzel:wght@700&family=Open+Sans:wght@400;600&display=swap" rel="stylesheet">
<style>
  :root{
    --navy:#1c3764;
    --navy-dark:#12264a;
    --accent:#c23b2e;
    --paper:#ffffff;
    --paper-shade:#eef0f3;
    --ink:#3d4350;
    --muted:#7a808c;
    --backdrop:#dcdfe3;
  }
  *{box-sizing:border-box;margin:0;padding:0}
  html,body{width:1200px;height:1002px;overflow:hidden}
  body{background:var(--backdrop);font-family:"Open Sans",sans-serif;color:var(--ink);position:relative}
  .piece{position:absolute;background:var(--paper);box-shadow:0 4px 14px rgba(0,0,0,.18)}

  .brand{display:flex;align-items:center;gap:8px}
  .brand-mark{width:18px;height:18px;background:var(--navy);flex:none}
  .brand-name{font-family:"Cinzel",serif;font-weight:700;color:var(--navy);letter-spacing:.5px;line-height:1;white-space:nowrap}
  .brand--light .brand-mark{background:var(--paper)}
  .brand--light .brand-name{color:var(--paper)}

  /* Envelope back */
  .envelope-back{left:40px;top:40px;width:520px;height:240px;overflow:hidden;background:var(--paper-shade)}
  .envelope-back svg{position:absolute;inset:0}
  .envelope-back .flap-url{position:absolute;top:58px;width:100%;text-align:center;font-size:10px;color:#c9d3e4;letter-spacing:.5px}

  /* Envelope front */
  .envelope-front{left:40px;top:310px;width:520px;height:230px}
  .envelope-front .brand{position:absolute;left:26px;top:26px}
  .envelope-front .brand-name{font-size:17px}
  .envelope-front .return{position:absolute;left:52px;top:52px;font-size:8px;color:var(--muted)}

  /* Business cards */
  .card{width:336px;height:192px;border-radius:6px}
  .card-front{left:40px;top:575px}
  .card-front .brand{position:absolute;left:20px;top:24px;gap:6px}
  .card-front .brand-mark{width:14px;height:14px}
  .card-front .brand-name{font-size:11px}
  .card-front .person{position:absolute;left:20px;top:104px}
  .card-front .person-name{font-size:11px;font-weight:600;color:var(--navy)}
  .card-front .person-title{font-size:8px;color:var(--muted)}
  .card-front .address{position:absolute;left:20px;top:138px;font-size:8px;line-height:1.45;color:var(--ink);font-style:normal}
  .card-front .divider{position:absolute;left:186px;top:28px;width:1px;height:136px;background:#c9ced6}
  .card-front .contact{position:absolute;left:200px;top:30px;font-size:8px;line-height:1.6}
  .contact dt{float:left;width:30px;color:var(--accent);font-weight:600}
  .contact dd{margin-left:30px}

  .card-back{left:40px;top:790px;background:linear-gradient(160deg,var(--navy) 0%,var(--navy-dark) 100%);overflow:hidden}
  .card-back .brand{position:absolute;left:22px;top:120px}
  .card-back .brand-name{font-size:15px}
  .card-back .web{position:absolute;left:48px;top:146px;font-size:8px;color:#c9d3e4}

  /* Letterhead */
  .letterhead{left:604px;top:60px;width:560px;height:792px}
  .letterhead .top-rule{position:absolute;left:0;right:0;top:14px;height:4px;background:var(--navy)}
  .letterhead .brand{position:absolute;left:44px;top:48px}
  .letterhead .brand-name{font-size:20px}
  .letterhead .header-rule{position:absolute;left:44px;right:44px;top:88px;height:1px;background:var(--accent)}
  .letterhead .footer-rule{position:absolute;left:44px;right:44px;bottom:62px;height:1px;background:var(--navy)}
  .letterhead .footer{position:absolute;left:44px;right:44px;bottom:30px;text-align:center;font-size:8px;line-height:1.6;color:var(--muted)}
</style>
</head>
<body>

  <section class="piece envelope-back" aria-label="Envelope back">
    <svg width="520" height="240" viewBox="0 0 520 240">
      <polygon points="0,0 520,0 260,150" fill="var(--navy)"/>
      <polyline points="0,240 260,120 520,240" fill="none" stroke="#d3d7de" stroke-width="1"/>
    </svg>
    <p class="flap-url">www.trclaimpro.com</p>
  </section>

  <section class="piece envelope-front" aria-label="Envelope front">
    <div class="brand"><span class="brand-mark"></span><span class="brand-name">TR Claim Advisors</span></div>
    <p class="return">Suffolk Office, 205 Ridge Rd, Hauppauge, NY 11788</p>
  </section>

  <section class="piece card card-front" aria-label="Business card, information side">
    <div class="brand"><span class="brand-mark"></span><span class="brand-name">TR Claim Advisors</span></div>
    <div class="person">
      <p class="person-name">Doran T. Whitcombe</p>
      <p class="person-title">Sr. Public Adjuster</p>
    </div>
    <address class="address">
      58 W. Alder St.<br>Suite 612<br>Smithtown, NY 11492
    </address>
    <span class="divider"></span>
    <dl class="contact">
      <dt>Tel:</dt><dd>516.843.9076</dd>
      <dt>Fax:</dt><dd>516.843.9075</dd>
      <dt>Cell:</dt><dd>516.843.9077</dd>
      <dt>Email:</dt><dd>doran@trclaimpro.com</dd>
      <dt>Web:</dt><dd>www.trclaimpro.com</dd>
    </dl>
  </section>

  <section class="piece card card-back" aria-label="Business card, logo side">
    <div class="brand brand--light"><span class="brand-mark"></span><span class="brand-name">TR Claim Advisors</span></div>
    <p class="web">www.trclaimpro.com</p>
  </section>

  <section class="piece letterhead" aria-label="Letterhead">
    <span class="top-rule"></span>
    <div class="brand"><span class="brand-mark"></span><span class="brand-name">TR Claim Advisors</span></div>
    <span class="header-rule"></span>
    <span class="footer-rule"></span>
    <p class="footer">Suffolk Office, 205 Ridge Rd, Hauppauge, NY 11788<br>Tel: 516.843.9076 &nbsp;·&nbsp; Fax: 516.843.9075 &nbsp;·&nbsp; www.trclaimpro.com</p>
  </section>

</body>
</html>
```